Business cards, envelopes, etc. for real estate company

We have a finished logo for our real estate company. We need a corporate identity package with the following items:

1. Business Cards
2. Letterhead/Stationary - with 2 pages:
-1st page with full header
-2nd page without top header
3. Concise and professional e-mail signature image
4. Fax coversheet
5. Shipping label, with our return address and a mail-to address (on one label)

We need these to be editable. We don't know the industry standard for these items but perhaps you can provide them to us in .PDF and Word format (and if you use Adobe Illustrator for them, .AI as well).

Please use the attached placeholder logo in your design entry. We will provide you with the original logo to swap in (same size and design, just different text) when we choose your entry.

Please include the following information on the letterhead and business cards:

58 Birchwell Road
Suite 2B West
New York, NY 10587

Tel: 555-014-2837
Fax :555-014-2837

Please contact us if you have any questions about this contest.

Hi,

Thanks for your interest in this project. The logo to use should be working now. Please contact me if you have any further issues or questions.

I look forward to seeing your submissions. 

Hi,

We first wish to thank you all for your submissions. 

Here is some general feedback regarding the designs shown:

1. We would prefer square (as opposed to rounded) business cards.

2. For the fax coversheets, we are looking with a designed look. While we understand these are samples, we don't want it to appear as if it a standard block of text or a fax template from a word processing program.

3. For the 1st page of letterhead and envelopes, we do need an office address on them. The envelopes should have space for a stamp in the top right corner. We would prefer the envelopes not to have colored stripes.

4. We think a watermark of the logo is an interesting idea on the business cards and/or letterhead. This may be something to try. However, it is not strictly necessary and we would like to evaluate designs with and without it.

In general we are looking for a clean yet professional look.

We are actively reviewing all entries and thank you for your time and creativity.

One last comment: We understand making all objects in the brief takes some time. However, we want to remind all the designers that this contest is for more than just business cards (envelopes, letterheads, etc.) so if we choose your design, those items will be expected. Please refer to the original brief to see what we are requesting.

If you provide a mockup of any item listed in the brief (in addition to business cards) it would help us visualize your entire vision for this project.

```html
<!DOCTYPE html>
<html lang="en">
<head>
<meta charset="utf-8">
<title>Halden &amp; Halden – Stationery Set</title>
<link rel="stylesheet" href="https://fonts.googleapis.com/css2?family=Mulish:wght@400;600&display=swap">
<style>
  :root {
    --brand-teal: #24505f;
    --brand-grey: #7d8387;
    --paper: #ffffff;
    --stage: #5d5f61;
    --label: #f2f2f2;
    --shadow: 0 3px 8px rgba(0,0,0,.45);
  }
  * { box-sizing: border-box; margin: 0; padding: 0; }
  html, body { width: 1200px; height: 866px; overflow: hidden; }
  body {
    background: var(--stage);
    font-family: "Mulish", sans-serif;
    position: relative;
  }
  .label {
    position: absolute;
    color: var(--label);
    font-size: 14px;
    font-weight: 600;
    letter-spacing: .3px;
    transform: translateX(-50%);
    white-space: nowrap;
  }
  .sheet {
    position: absolute;
    background: var(--paper);
    box-shadow: var(--shadow);
    overflow: hidden;
  }

  /* brand lockup: plain square + name */
  .brand { position: absolute; display: flex; align-items: center; }
  .brand__square { background: var(--brand-teal); flex: none; }
  .brand__name {
    color: var(--brand-grey);
    font-weight: 400;
    line-height: 1.05;
  }
  .brand--lg .brand__square { width: 54px; height: 54px; margin-right: 10px; }
  .brand--lg .brand__name { font-size: 27px; }
  .brand--sm .brand__square { width: 26px; height: 26px; margin-right: 5px; }
  .brand--sm .brand__name { font-size: 12px; }
  .brand--reverse .brand__square { background: #ffffff; }
  .brand--reverse .brand__name { color: #ffffff; }

  /* business card */
  .card-front { left: 67px; top: 60px; width: 227px; height: 131px; background: var(--brand-teal); }
  .card-front .brand { left: 12px; bottom: 12px; }
  .card-back { left: 325px; top: 60px; width: 227px; height: 131px; }
  .card-back__person { position: absolute; left: 21px; top: 19px; }
  .card-back__name { font-size: 10px; color: var(--brand-teal); font-weight: 600; }
  .card-back__title { font-size: 6.5px; color: var(--brand-grey); }
  .card-back__contact {
    position: absolute; left: 21px; top: 68px;
    font-size: 5.5px; line-height: 1.4; color: var(--brand-grey);
  }
  .card-back__contact strong { color: var(--brand-teal); font-weight: 600; }
  .card-back .brand { right: 20px; bottom: 16px; }

  /* envelopes & letterhead footer band */
  .address-band {
    position: absolute; left: 0; right: 0; bottom: 0;
    background: var(--brand-teal);
    color: #ffffff;
    display: flex; align-items: center; justify-content: center;
    font-size: 9.5px; letter-spacing: .2px;
  }
  .envelope-front { left: 19px; top: 242px; width: 584px; height: 262px; }
  .envelope-front .brand { left: 25px; top: 27px; }
  .envelope-front .address-band { height: 29px; bottom: 3px; }
  .envelope-back { left: 19px; top: 545px; width: 584px; height: 261px; }
  .envelope-back__flap {
    position: absolute; left: 0; top: 0; width: 100%; height: 78px;
    background: var(--brand-teal);
    border-radius: 0 0 18px 18px;
  }

  .letterhead { left: 645px; top: 43px; width: 536px; height: 758px; }
  .letterhead .brand { left: 32px; top: 33px; }
  .letterhead .address-band { height: 34px; }
</style>
</head>
<body>

  <span class="label" style="left:170px; top:29px;">Front</span>
  <span class="label" style="left:298px; top:19px;">Business Card</span>
  <span class="label" style="left:432px; top:31px;">Back</span>

  <section class="sheet card-front" aria-label="Business card front">
    <div class="brand brand--sm brand--reverse">
      <span class="brand__square"></span>
      <span class="brand__name">Halden<br>&amp; Halden</span>
    </div>
  </section>

  <section class="sheet card-back" aria-label="Business card back">
    <div class="card-back__person">
      <p class="card-back__name">Your Name</p>
      <p class="card-back__title">Your Designation</p>
    </div>
    <div class="card-back__contact">
      <p><strong>Halden &amp; Halden</strong></p>
      <p>58 Birchwell Road</p>
      <p>Suite 2B West</p>
      <p>New York, NY 10587</p>
      <p><strong>Tel:</strong> 555-014-2837</p>
      <p><strong>Fax:</strong> 555-014-2837</p>
    </div>
    <div class="brand brand--sm">
      <span class="brand__square"></span>
      <span class="brand__name">Halden<br>&amp; Halden</span>
    </div>
  </section>

  <span class="label" style="left:307px; top:213px;">Envelope DL</span>

  <section class="sheet envelope-front" aria-label="DL envelope front">
    <div class="brand brand--lg">
      <span class="brand__square"></span>
      <span class="brand__name">Halden<br>&amp; Halden</span>
    </div>
    <p class="address-band">58 Birchwell Road, Suite 2B West, New York, NY 10587 | Tel: 555-014-2837 | Fax: 555-014-2837</p>
  </section>

  <span class="label" style="left:306px; top:512px;">Front</span>

  <section class="sheet envelope-back" aria-label="DL envelope back">
    <div class="envelope-back__flap"></div>
  </section>

  <span class="label" style="left:313px; top:813px;">Back</span>

  <section class="sheet letterhead" aria-label="Letterhead">
    <div class="brand brand--lg">
      <span class="brand__square"></span>
      <span class="brand__name">Halden<br>&amp; Halden</span>
    </div>
    <p class="address-band">58 Birchwell Road, Suite 2B West, New York, NY 10587 | Tel: 555-014-2837 | Fax: 555-014-2837</p>
  </section>

  <span class="label" style="left:910px; top:810px;">Letter Head</span>

</body>
</html>
```